Website design using a wordpress template I purchased

I have purchased a wordpress template called "Vantrel" from Plumora and would like to design a website using it for a financial services company. The site simply needs to be informational about the company and a blog. Nothing too involved. The company provides paymaster / escrow services for commodity transactions. I am working on the logo currently and will have it ready to provide shortly. I can provide the content for the informational portion of the site as well. I would like some quick tutoring regarding how to administer the blog portion of the site once built.

```html
<!DOCTYPE html>
<html lang="en">
<head>
<meta charset="utf-8">
<title>Financial Services</title>
<link rel="stylesheet" href="https://fonts.googleapis.com/css2?family=Cabin:wght@400;500;600;700&family=Lato:wght@300;400;700&family=Poppins:wght@400;500;600&family=Roboto+Slab:wght@400&display=swap">
<style>
:root{
  --blue:#3d85e6;
  --blue-soft:#4f7fe0;
  --pale:#eef5fe;
  --ink:#111111;
  --muted:#5b5b5b;
  --grey-bg:#f5f6f8;
  --white:#ffffff;
  --black:#000000;
}
*{margin:0;padding:0;box-sizing:border-box}
html,body{width:1200px;height:2768px;overflow:hidden;background:var(--white)}
body{font-family:'Lato',sans-serif;color:var(--ink)}
.page{position:relative;width:1200px;height:2768px;overflow:hidden}
.abs{position:absolute}

/* hero */
.hero-bg{left:0;top:0;width:1200px;height:640px;background:var(--pale)}
.hero-blue{left:0;top:0;width:727px;height:640px;background:linear-gradient(135deg,#3a8ae6 0%,#357fe2 50%,#4a7ee0 100%);overflow:hidden}
.hero-blue svg{position:absolute;left:0;top:0}
.brand{left:93px;top:38px;font-family:'Cabin',sans-serif;font-weight:700;font-size:25px;color:var(--white)}
.nav{left:420px;top:45px;display:flex;gap:34px;font-family:'Lato',sans-serif;font-size:15px;color:var(--white)}
.nav .active{font-weight:700;text-decoration:underline;text-underline-offset:3px}
.hero-title{left:91px;top:186px;font-family:'Cabin',sans-serif;font-weight:500;font-size:53px;line-height:56px;color:var(--white)}
.hero-text{left:95px;top:304px;width:400px;font-size:14.5px;font-weight:300;line-height:26px;color:var(--white)}
.btn-white{background:var(--white);color:var(--ink);font-family:'Cabin',sans-serif;font-weight:600;font-size:20px;display:flex;align-items:center;justify-content:center}
.hero-btn{left:95px;top:395px;width:135px;height:51px}
.hero-photo{left:541px;top:129px;width:546px;height:383px;background:linear-gradient(135deg,#c9d3dc 0%,#8c9aa8 45%,#3f4c5c 100%)}
.play{left:788px;top:294px;width:46px;height:46px;border-radius:50%;background:var(--black)}

/* news */
.section-title{font-family:'Cabin',sans-serif;font-weight:700;font-size:37px;text-align:center;width:1200px;left:0}
.section-title span{color:var(--blue)}
.news-title{top:708px}
.news-sub{left:0;top:760px;width:1200px;text-align:center;font-size:14px;font-weight:300;line-height:27px;color:#333}
.card{top:829px;width:298px;height:363px;background:var(--white);box-shadow:0 4px 14px rgba(0,0,0,.12);text-align:center}
.card.featured{border:1px solid var(--blue)}
.card-img{position:absolute;left:0;top:0;width:100%;height:225px}
.card-head{position:absolute;left:10px;top:194px;width:278px;height:32px;background:var(--white);font-family:'Cabin',sans-serif;font-weight:500;font-size:19px;padding-top:6px}
.card-date{position:absolute;left:0;top:236px;width:100%;font-size:11px;font-weight:400}
.card-text{position:absolute;left:14px;top:250px;width:270px;font-size:15px;font-weight:300;line-height:25px;color:var(--muted)}
.card-link{position:absolute;left:0;top:328px;width:100%;font-family:'Roboto Slab',serif;font-size:14px;text-decoration:underline}
.featured .card-head,.featured .card-date,.featured .card-link{color:var(--blue)}

/* about */
.about-band{left:0;top:1281px;width:1200px;height:475px;background:linear-gradient(90deg,#3b87e6,#4f84e6)}
.about-photo{left:112px;top:1351px;width:432px;height:438px;background:linear-gradient(120deg,#d7d3cb 0%,#b7aea2 45%,#3b3d44 100%)}
.about-title{left:614px;top:1343px;font-family:'Cabin',sans-serif;font-weight:700;font-size:37px;color:var(--white)}
.about-text{left:616px;top:1389px;width:472px;font-size:14.5px;font-weight:300;line-height:27.4px;color:var(--white)}
.about-text p+p{margin-top:27px}
.about-btn{left:614px;top:1645px;width:136px;height:51px}

/* contact */
.contact-bg{background:var(--grey-bg)}
.contact-title{top:1828px}
.info-icon{left:110px;width:60px;height:60px;border-radius:50%;background:var(--blue);display:flex;align-items:center;justify-content:center}
.info-label{left:188px;font-family:'Poppins',sans-serif;font-size:15px;font-weight:500;color:#222}
.info-value{left:188px;font-family:'Poppins',sans-serif;font-size:15px;font-weight:400;line-height:24px;color:#555}
.field{background:var(--white);font-family:'Roboto',sans-serif;font-size:14.5px;color:#555;padding:16px 17px;box-shadow:0 1px 3px rgba(0,0,0,.05)}
.submit{left:510px;top:2172px;width:136px;height:51px;background:var(--blue-soft);color:var(--white);font-family:'Cabin',sans-serif;font-weight:700;font-size:20px;display:flex;align-items:center;justify-content:center}

/* footer */
.footer{left:0;top:2333px;width:1200px;height:435px;background:var(--black);color:var(--white);font-family:'Poppins',sans-serif}
.foot-head{top:90px;font-family:'Poppins',sans-serif;font-weight:600;font-size:21px}
.foot-list{top:136px;list-style:none;font-size:16px;line-height:34.4px}
.foot-list li::before{content:"";display:inline-block;width:5px;height:5px;border:1.5px solid var(--white);border-radius:50%;margin-right:9px;vertical-align:middle}
.foot-contact{font-size:15.5px;line-height:24px;display:flex;align-items:center;gap:11px}
.ring{width:29px;height:29px;border-radius:50%;border:2px solid var(--white);display:flex;align-items:center;justify-content:center;flex:none}
.foot-about{left:866px;top:138px;width:220px;font-size:12.5px;line-height:26px}
.social{top:260px;width:26px;height:26px;border-radius:50%;background:var(--blue-soft)}
.divider{left:111px;top:357px;width:977px;height:1px;background:#cfcfcf}
.copyright{left:0;top:387px;width:1200px;text-align:center;font-size:12.5px;font-weight:500}
</style>
</head>
<body>
<div class="page">

  <div class="abs hero-bg"></div>
  <div class="abs hero-blue">
    <svg width="727" height="640" viewBox="0 0 727 640">
      <polygon points="0,640 0,520 460,0 727,0 727,120 150,640" fill="#ffffff" opacity="0.05"/>
      <polygon points="0,640 727,200 727,640" fill="#3a6fd8" opacity="0.25"/>
    </svg>
  </div>
  <div class="abs brand">Financial Services</div>
  <nav class="abs nav">
    <span class="active">Home</span><span>About</span><span>Blog</span><span>Contact Us</span>
  </nav>
  <h1 class="abs hero-title">Welcome To<br>Financial Services</h1>
  <p class="abs hero-text">Quis autem vel eum iure reprehenderit qui in ea voluptate velit esse quam nihil molestiae consequatur, vel illum qui dolorem eum fugiat quo voluptas nulla pariatur.</p>
  <div class="abs btn-white hero-btn">Get Started</div>
  <div class="abs hero-photo" role="img" aria-label="Photo of two smiling businessmen in suits at a meeting table"></div>
  <div class="abs play">
    <svg width="46" height="46" viewBox="0 0 46 46"><polygon points="18,14 32,23 18,32" fill="#ffffff"/></svg>
  </div>

  <h2 class="abs section-title news-title">Latest <span>News</span></h2>
  <p class="abs news-sub">Ut enim ad minima veniam, quis nostrum exercitationem ullam corporis suscipit laboriosam, nisi ut<br>aliquid ex ea commodi consequatur.</p>

  <article class="abs card" style="left:111px">
    <div class="card-img" role="img" aria-label="Photo of hands holding a phone with star rating graphics" style="background:linear-gradient(135deg,#2b3a4a,#46596c 50%,#8a6d3a)"></div>
    <div class="card-head">Dignissimos ducimus</div>
    <div class="card-date">12, May 2022</div>
    <p class="card-text">Itaque earum rerum hic tenetur a<br>sapiente delectus, ut aut reiciendis<br>voluptatibus maiores</p>
    <div class="card-link">Read More</div>
  </article>

  <article class="abs card featured" style="left:450px">
    <div class="card-img" role="img" aria-label="Photo of a smiling woman recorded by a camera" style="background:linear-gradient(135deg,#dfe6ea,#c9d4da 55%,#e8b9b4)"></div>
    <div class="card-head">Praesentium voluptatum</div>
    <div class="card-date">22, June 2022</div>
    <p class="card-text">Alias consequatur aut maxime placeat<br>facere possimus perferendis doloribus<br>asperiores repellat.</p>
    <div class="card-link">Read More</div>
  </article>

  <article class="abs card" style="left:789px">
    <div class="card-img" role="img" aria-label="Photo of three colleagues leaning over a desk reviewing papers" style="background:linear-gradient(135deg,#b8c2cc,#8f9aa6 50%,#c6a24a)"></div>
    <div class="card-head">Expedita distinctio Nam</div>
    <div class="card-date">12, May 2022</div>
    <p class="card-text">Temporibus autem quibusdam et aut<br>officiis debitis aut rerum necessitatibus<br>saepe eveniet ut et voluptates</p>
    <div class="card-link">Read More</div>
  </article>

  <div class="abs about-band"></div>
  <div class="abs about-photo" role="img" aria-label="Photo of a smiling woman shaking hands with a businessman"></div>
  <h2 class="abs about-title">About Financial Services</h2>
  <div class="abs about-text">
    <p>Et harum quidem rerum facilis est et expedita distinctio. Nam libero tempore, cum soluta nobis est eligendi optio cumque nihil impedit quo minus id quod maxime placeat facere possimus, omnis voluptas assumenda est, omnis dolor repellendus. Temporibus autem quibusdam et aut officiis sint et molestiae non recusandae.</p>
    <p>Itaque earum rerum hic tenetur a sapiente delectus, ut aut reiciendis voluptatibus maiores alias consequatur aut perferendis doloribus asperiores repellat.</p>
  </div>
  <div class="abs btn-white about-btn">Read More</div>

  <div class="abs contact-bg" style="left:0;top:1789px;width:1200px;height:544px"></div>
  <div class="abs contact-bg" style="left:544px;top:1756px;width:656px;height:33px"></div>
  <div class="abs contact-bg" style="left:0;top:1756px;width:112px;height:33px"></div>
  <h2 class="abs section-title contact-title">Get In Touch <span>With Us</span></h2>

  <div class="abs info-icon" style="top:1920px">
    <svg width="22" height="22" viewBox="0 0 24 24"><path d="M12 2a7 7 0 0 0-7 7c0 5 7 13 7 13s7-8 7-13a7 7 0 0 0-7-7zm0 9.5A2.5 2.5 0 1 1 12 6.5a2.5 2.5 0 0 1 0 5z" fill="#fff"/></svg>
  </div>
  <div class="abs info-label" style="top:1916px">ADDRESS:</div>
  <div class="abs info-value" style="top:1943px">Financial Services<br>United States</div>

  <div class="abs info-icon" style="top:2023px">
    <svg width="22" height="22" viewBox="0 0 24 24"><path d="M6.6 10.8a15 15 0 0 0 6.6 6.6l2.2-2.2c.3-.3.7-.4 1-.2 1.1.4 2.3.6 3.6.6.6 0 1 .4 1 1V20c0 .6-.4 1-1 1A17 17 0 0 1 3 4c0-.6.4-1 1-1h3.5c.6 0 1 .4 1 1 0 1.3.2 2.5.6 3.6.1.3 0 .7-.2 1z" fill="#fff"/></svg>
  </div>
  <div class="abs info-label" style="top:2027px">PHONE:</div>
  <div class="abs info-value" style="top:2055px">+1 555 204 7319</div>

  <div class="abs info-icon" style="top:2119px">
    <svg width="22" height="22" viewBox="0 0 24 24"><path d="M3 6h18v12H3z" fill="#fff"/><path d="M3 6l9 7 9-7" fill="none" stroke="#3d85e6" stroke-width="1.8"/></svg>
  </div>
  <div class="abs info-label" style="top:2122px">EMAIL:</div>
  <div class="abs info-value" style="top:2150px">info@northquill-finance.com</div>

  <div class="abs field" style="left:510px;top:1911px;width:283px;height:49px">First Name</div>
  <div class="abs field" style="left:803px;top:1911px;width:283px;height:49px">Last Name</div>
  <div class="abs field" style="left:510px;top:1973px;width:283px;height:49px">Your Phone</div>
  <div class="abs field" style="left:803px;top:1973px;width:283px;height:49px">Your Email</div>
  <div class="abs field" style="left:510px;top:2037px;width:576px;height:111px">Message</div>
  <div class="abs submit">Submit</div>

  <footer class="abs footer">
    <div class="abs foot-head" style="left:111px">Quick Links</div>
    <ul class="abs foot-list" style="left:111px">
      <li>Home</li><li>About</li><li>Services</li><li>Intensives</li><li>Contact</li>
    </ul>

    <div class="abs foot-head" style="left:320px">Help Links</div>
    <ul class="abs foot-list" style="left:320px">
      <li>Faq</li><li>Term of Use</li><li>Support Links</li><li>Privacy Policy</li><li>Terms &amp; Conditions</li>
    </ul>

    <div class="abs foot-head" style="left:558px">Contact Us</div>
    <div class="abs foot-contact" style="left:558px;top:134px">
      <span class="ring"><svg width="14" height="14" viewBox="0 0 24 24"><path d="M6.6 10.8a15 15 0 0 0 6.6 6.6l2.2-2.2c.3-.3.7-.4 1-.2 1.1.4 2.3.6 3.6.6.6 0 1 .4 1 1V20c0 .6-.4 1-1 1A17 17 0 0 1 3 4c0-.6.4-1 1-1h3.5c.6 0 1 .4 1 1 0 1.3.2 2.5.6 3.6.1.3 0 .7-.2 1z" fill="#4f7fe0"/></svg></span>
      +1 555 204 7319
    </div>
    <div class="abs foot-contact" style="left:558px;top:178px">
      <span class="ring"><svg width="14" height="14" viewBox="0 0 24 24"><path d="M12 2a7 7 0 0 0-7 7c0 5 7 13 7 13s7-8 7-13a7 7 0 0 0-7-7zm0 9.5A2.5 2.5 0 1 1 12 6.5a2.5 2.5 0 0 1 0 5z" fill="#4f7fe0"/></svg></span>
      <span>Financial Services<br>United States</span>
    </div>
    <div class="abs foot-contact" style="left:558px;top:244px">
      <span class="ring"><svg width="14" height="14" viewBox="0 0 24 24"><path d="M3 6h18v12H3z" fill="#4f7fe0"/><path d="M3 6l9 7 9-7" fill="none" stroke="#fff" stroke-width="2"/></svg></span>
      info@northquill-finance.com
    </div>

    <div class="abs foot-head" style="left:866px">About Financial Services</div>
    <p class="abs foot-about">Excepteur sint occaecat cupidatat non proident, sunt in culpa qui officia deserunt mollit anim id est laborum."</p>
    <span class="abs social" style="left:866px"></span>
    <span class="abs social" style="left:915px"></span>
    <span class="abs social" style="left:964px"></span>
    <span class="abs social" style="left:1013px"></span>

    <div class="abs divider"></div>
    <div class="abs copyright">Copyrights@2022.Financial Services.All Rights Reserved</div>
  </footer>

</div>
</body>
</html>
```